Tri-Fold Brochure for Christian Author and Speaker

Lorena Watkiss is an inspirational author and speaker, sharing her testimony and encouraging others in their walk with Christ. A gifted writer, her work has been featured on Gently Radiant, Morning Vessels, and Hymn & Tea Journal (Fall 2011).

Lorena ‘s first book, Leaving the Lantern Hall: Revealing Hidden Snares in Ordinary Routines, is an informative memoir and Bible study, recounting her journey from committed Christian to witch, medium, and ghost hunter for eight years until restored to faith in Jesus Christ. She was a contributing author to Walking the Shadow Road: A Plain Account of Dark Arts from Past Seekers by Dale Winterbottom and a consultant for the novel The Keeper of Pellam Hollow by Lumen Prize Winning Author, Norma Quillfeather.

Lorena’s second book, An Insider’s Guide to Spiritual Warfare: 20 Battle-Tested Strategies from Behind Enemy Lines, will be published by Ridgeway Press for Fall 2014.

Lorena is a wife and mother. She enjoys writing, spending time with her family, taking long walks, listening to music of all kinds, and experiencing God’s daily gift called life.

You can read more about Lorena and see the look and feel we are going for at www.lorenawatkiss.example

The brochure is to be used as a promotional tool to gain Lorena speaking engagements. You can see the topics she covers at http://www.lorenawatkiss.example/speaking-engagements/.

More info can be found at: https://www.social.example/AuthorLorenaWatkiss
https://www.social.example/VMUCX
https://www.social.example/LeavingtheLanternHall
https://www.social.example/TallOakOutreach
http://www.talloakoutreach.example

I have uploaded 3 headshots, book covers for both of Lorena's books and the design layout in .EPS format from Quickprintly.example where I will be getting printing done.

3 more days till the contest ends get your final designs in.

Reason: I'm extending this as I am tied up at a leadership conference and will not be able to give this the attention it deserves till the weekend.

Target Market(s)

Churches and women's groups. Lorena's current audience skews heavy to women on a 70/30 ratio.

Industry/Entity Type

Christian

Requirements
Must have
• Headshot I have uploaded 3
Quotes from previous speaking engagements you can find those at http://www.lorenawatkiss.example/speaking-engagements/

```html
<!DOCTYPE html>
<html lang="en">
<head>
<meta charset="utf-8">
<title>Lorena Watkiss – Tri-Fold Brochure</title>
<link href="https://fonts.googleapis.com/css2?family=Cinzel:wght@400;600&family=Old+Standard+TT:ital,wght@0,400;0,700;1,400&family=Open+Sans:wght@700&display=swap" rel="stylesheet">
<style>
  :root{
    --wine:#7a1a2e;
    --wine-dark:#4a0c18;
    --ink:#3a2a2e;
    --blush:#f6ebf0;
    --petal:#e7b6c8;
    --rose:#c98aa2;
    --sky:#cdd8ea;
    --page:#e6e6e6;
    --white:#ffffff;
    --black:#0c0c0c;
  }
  *{box-sizing:border-box;margin:0;padding:0}
  html,body{width:733px;height:1200px;overflow:hidden}
  body{background:var(--page);position:relative;font-family:"Old Standard TT",Georgia,serif;color:var(--ink)}

  .spread{position:absolute;left:21px;width:690px;height:540px;display:flex;box-shadow:0 2px 8px rgba(0,0,0,.18);
    background:
      radial-gradient(ellipse at 55% 20%, rgba(231,182,200,.55), transparent 55%),
      radial-gradient(ellipse at 85% 85%, rgba(205,216,234,.6), transparent 50%),
      radial-gradient(ellipse at 15% 70%, rgba(231,182,200,.35), transparent 55%),
      var(--blush);}
  .spread--outside{top:40px}
  .spread--inside{top:620px}
  .panel{position:relative;width:230px;height:100%;overflow:hidden}
  .panel + .panel{border-left:1px solid rgba(122,26,46,.12)}

  .photo{background:linear-gradient(160deg,#6f7d55 0%,#a56a55 45%,#5b2a22 100%)}
  .photo--speaker{background:linear-gradient(170deg,#b9a7a3 0%,#6b4c47 45%,#1f1a1c 100%)}

  /* Outside – meet panel */
  .meet__header{height:46px;background:var(--black);color:var(--white);font-family:"Cinzel",serif;font-size:15px;text-align:right;padding:13px 16px 0 0;letter-spacing:1px}
  .meet__photo{position:absolute;top:50px;left:55px;width:125px;height:95px}
  .meet__bio{position:absolute;top:158px;left:16px;right:14px;font-style:italic;font-size:8.4px;line-height:11.4px;text-align:left}
  .meet__bio p{margin-bottom:7px}

  /* Outside – books panel */
  .books__title{margin-top:40px;text-align:center;font-family:"Cinzel",serif;color:var(--wine);font-size:15px;line-height:18px;letter-spacing:1px}
  .books__grid{display:grid;grid-template-columns:86px 86px;gap:14px 14px;justify-content:center;margin-top:30px}
  .book{height:124px;box-shadow:1px 2px 4px rgba(0,0,0,.3)}
  .book--shadow{background:linear-gradient(180deg,#1a1416,#3b0d10 60%,#a0241c)}
  .book--warfare{background:linear-gradient(160deg,#2f6a2a,#9cc43a 50%,#1a3a1e)}
  .book--lantern{background:linear-gradient(180deg,#8a8a8a,#e8e4df 55%,#c9b8a0)}
  .book--hollow{background:linear-gradient(180deg,#0d0c10,#2a1a14 60%,#c9741c)}

  /* Outside – cover panel */
  .cover__photo{position:absolute;top:0;left:0;width:230px;height:250px}
  .cover__name{position:absolute;top:278px;left:0;right:0;text-align:center;font-family:"Cinzel",serif;color:var(--wine);font-size:38px;line-height:44px}
  .cover__tagline{position:absolute;top:400px;left:0;right:0;text-align:center;font-family:"Cinzel",serif;color:var(--wine);font-size:13px;line-height:19px;letter-spacing:.5px}

  /* Inside */
  .masthead{position:absolute;top:0;left:0;width:690px;height:92px;background:linear-gradient(90deg,rgba(201,138,162,.75),rgba(231,182,200,.7) 45%,rgba(205,216,234,.9) 80%,rgba(231,182,200,.6))}
  .masthead__photo{position:absolute;top:0;left:0;width:48px;height:92px}
  .masthead__name{position:absolute;top:50px;left:52px;font-family:"Cinzel",serif;color:var(--wine);font-size:34px;line-height:38px;letter-spacing:.5px}
  .masthead__role{position:absolute;top:60px;left:476px;font-family:"Cinzel",serif;color:var(--wine);font-size:17px;line-height:22px;letter-spacing:.5px}
  .inside__panel{padding-top:96px}
  .col{padding:0 10px 0 12px;font-size:8.2px;line-height:10.4px}
  .col--middle{font-size:8px;line-height:10px}
  .quote__by{font-weight:700;font-size:9.6px;line-height:11px;color:var(--black);margin:6px 0 4px}
  .quote__text{font-style:italic;margin-bottom:4px}

  .intro{overflow:hidden;margin:0 0 0 -12px}
  .intro__photo{float:left;width:66px;height:148px;margin-right:8px}
  .intro__text{font-style:italic;font-size:9.2px;line-height:12px;padding-top:4px;padding-right:4px}
  .ask-bar{background:var(--wine-dark);color:var(--white);font-family:"Open Sans",Arial,sans-serif;font-weight:700;font-size:11.5px;padding:7px 0 7px 14px;margin:0 -10px 4px -12px}

  /* Middle column wraps around the topics box */
  .spacer-top{float:right;width:0;height:150px}
  .spacer-box{float:right;clear:right;width:98px;height:168px}
  .topics{position:absolute;top:250px;left:360px;width:92px;background:var(--wine-dark);color:var(--white);padding:6px 5px;font-size:7.5px;line-height:9.5px;text-align:center;box-shadow:0 1px 4px rgba(0,0,0,.3)}
  .topics__title{font-size:10px;font-weight:700;margin-bottom:4px}
  .topics li{list-style:none;padding:4px 0;border-top:1px solid rgba(255,255,255,.35)}
</style>
</head>
<body>

<section class="spread spread--outside" aria-label="Brochure outside">
  <div class="panel meet">
    <div class="meet__header">Meet Lorena</div>
    <div class="meet__photo photo" role="img" aria-label="Headshot of Lorena Watkiss outdoors among greenery"></div>
    <div class="meet__bio">
      <p>Lorena Watkiss is an inspirational author and speaker, sharing her testimony and encouraging others in their walk with Christ. A gifted writer, her work has been featured on Gently Radiant, Morning Vessels, and Hymn &amp; Tea Journal (Fall 2011).</p>
      <p>Lorena's first book, Leaving the Lantern Hall: Revealing Hidden Snares in Ordinary Routines, is an informative memoir and Bible study, recounting her journey from committed Christian to witch, medium, and ghost hunter for eight years until restored to faith in Jesus Christ. She was a contributing author to Walking the Shadow Road by Dale Winterbottom and a consultant for The Keeper of Pellam Hollow by Lumen Prize Winning Author, Norma Quillfeather.</p>
      <p>Lorena's second book, A Veteran's Map for Unseen Conflict, will be published by Ridgeway Press for Fall 2014.</p>
      <p>Lorena is a wife and mother. She enjoys writing, spending time with her family, taking long walks, listening to music of all kinds, and experiencing God's daily gift called life.</p>
    </div>
  </div>

  <div class="panel books">
    <h2 class="books__title">Books by<br>Lorena Watkiss</h2>
    <div class="books__grid">
      <div class="book book--shadow" role="img" aria-label="Book cover: Walking the Shadow Road"></div>
      <div class="book book--warfare" role="img" aria-label="Book cover: A Veteran's Map for Unseen Conflict"></div>
      <div class="book book--lantern" role="img" aria-label="Book cover: Leaving the Lantern Hall"></div>
      <div class="book book--hollow" role="img" aria-label="Book cover: The Keeper of Pellam Hollow"></div>
    </div>
  </div>

  <div class="panel cover">
    <div class="cover__photo photo" role="img" aria-label="Smiling headshot of Lorena Watkiss"></div>
    <h1 class="cover__name">Lorena<br>Watkiss</h1>
    <p class="cover__tagline">An Inspirational<br>Author And Speaker</p>
  </div>
</section>

<section class="spread spread--inside" aria-label="Brochure inside">
  <div class="masthead">
    <div class="masthead__photo photo" role="img" aria-label="Headshot of Lorena Watkiss"></div>
    <div class="masthead__name">Lorena Watkiss</div>
    <div class="masthead__role">Author | Speaker</div>
  </div>

  <div class="panel inside__panel">
    <div class="col">
      <div class="intro">
        <div class="intro__photo photo photo--speaker" role="img" aria-label="Lorena Watkiss speaking at an event"></div>
        <p class="intro__text">As a speaker, Lorena shares from her own life lessons and as a biblical Counselor, encouraging others toward a deeper walk with God. Lorena offers sound, heartfelt, and practical biblical advice on issues relevant to the 21st Century Christian</p>
      </div>
      <div class="ask-bar">Lorena Like As A Speaker?</div>
      <p class="quote__by">Nadia Ferrowby, Lakeshine Community Church Women's Ministry:</p>
      <p class="quote__text">The Women's Ministry at Lakeshine Church in Marlow Falls, MI invited Lorena Watkiss to speak at our Mother or Daughter Banquet earlier this month. I am so glad she accepted! We couldn't have chosen a speaker to fit in better than Lorena. She took our theme, "Instruments", and incorporated that into her speaking time with us. She used life examples and spoke directly into the hearts of the women and girls that attended our banquet. She even took time to speak to my teen aged daughters after the banquet as to why they should stay away from the paranormal. I highly recommend Lorena as a speaker and we hope to have her back at Lakeshine Church in the near future!</p>
    </div>
  </div>

  <div class="panel inside__panel">
    <div class="col col--middle">
      <div class="spacer-top"></div>
      <div class="spacer-box"></div>
      <p class="quote__by">Joan Pellerin, Hymn and Tea Women's Ministry Events:</p>
      <p class="quote__text">"Lorena came to our Hymn and Tea Night and shared her story, it was amazing! I've never seen women so riveted by a speaker! If you are in a position to bring Lorena to your church/event...do it!"</p>
      <p class="quote__by">Martin Hollesby, Kindred Crossing Seminar Tent, Coordinator:</p>
      <p class="quote__text">"I was honored and delighted to have Lorena Watkiss be one of our speakers in the "Kindred Crossing Seminar Tent" at Kindred Christian Music Festival in Harbor Bend (one of the nation's top 10 Christian music festivals). Lorena has a unique testimony and style of speaking that keeps people, young and old, engaged into the heart of her message. Her stories of involvement in the occult and her conclusion of how God rescued her from these traps, answers many of the questions that people often have, but are afraid to ask when dealing with the "supernatural". If you are looking for a great speaker with a testimony that is relevant in today's culture of "curiosity in the supernatural", I highly recommend Lorena Watkiss to be on the top of your list of considerations."</p>
      <p class="quote__by">Ellen Dorsey, Cedar Covenant Church, Women's Christmas Tea Coordinator:</p>
      <p class="quote__text">"We had Lorena speak at our Women's Tea. Even though the weather was terrible in the north country we had a good turnout and I</p>
    </div>
  </div>

  <div class="panel inside__panel">
    <div class="col">
      <p class="quote__text">had several women tell me afterwards how blessed they were with Lorena's message. The emphasis was on putting Christ first during the holidays and not getting so busy we forget what Christmas is really about. Lorena was an enthusiastic and wonderful from-the-heart speaker. We hope to have her back again!"</p>
      <p class="quote__by">Paul Vandermeer, Pastor, Hope Reformed Church:</p>
      <p class="quote__text">"Lorena Watkiss spoke at our church sharing with us her testimony which includes how she attempted to blend witchcraft with Christianity. Obviously, she discovered that there is no compromising of the Gospel and the Holy Spirit brought her back in an amazing way. Her story is gripping. It also serves as a warning to not blend religion "ala carte" and to pay close attention to the Word of God. Lorena notes well that we all have a spiritual hunger, and if we don't satisfy it with Christ and His Word, we may slip into any kind of spiritual offering. The church needs to hear her story. It is a wake up call to be aware of the continual influence of our culture pushing us into consideration of the paranormal and other strange spiritual activity. It is also a pointed reminder that we, the church, need to be on the offensive knowing what we believe and to be willing to share it with searching, hungry souls. Lorena rounds out her story with sound theology and giving praise and glory to God. I would highly recommend to you that you engage Lorena in speaking to your church groups."</p>
    </div>
  </div>

  <aside class="topics">
    <div class="topics__title">Speaking Topics</div>
    <ul>
      <li>Christians and the Occult</li>
      <li>Homelessness<br>(with Ben Watkiss)</li>
      <li>Human Trafficking</li>
      <li>Marriage Restoration<br>(with Ben Watkiss)</li>
      <li>Prayer as a Lifestyle</li>
      <li>Spiritual Warfare</li>
    </ul>
  </aside>
</section>

</body>
</html>
```